BPR Business Card

We need a business card that reflect our business, we have put anther business card as an example of what we like but please feel free to do your own thing.

Here are the items to be placed on card

Glen Harwick
Bright Parcel Route
Mobile: 917-555-4862
Office: 516-555-7104
Fax: 866-555-3927
Email: info@brightparcelroute.example
Website: brightparcelroute.example

I have added raw files to upload

Glen Harwick
Bright Parcel Route
Mobile: 917-555-4862
Office: 516-555-7104
Fax: 866-555-3927 

Target Market(s)

Natural product manufactures, and retailers and distributors

Industry/Entity Type

Business

Requirements
Must have
• 1. Logo
2. The colors of the company

```html
<!DOCTYPE html>
<html lang="en">
<head>
<meta charset="utf-8">
<title>BPR Business Card</title>
<link rel="stylesheet" href="https://fonts.googleapis.com/css2?family=Arimo:wght@400;700&display=swap">
<style>
  :root {
    --stage: #2b2b2b;
    --leaf: #7cc21f;
    --leaf-dark: #4f8f12;
    --ink: #111111;
    --paper: #ffffff;
    --wash: #eef5e6;
    --muted: #444444;
  }
  * { box-sizing: border-box; margin: 0; padding: 0; }
  html, body { width: 1200px; height: 900px; overflow: hidden; }
  body {
    background: var(--stage);
    font-family: "Arimo", Arial, sans-serif;
    display: flex;
    align-items: center;
    justify-content: center;
    gap: 60px;
  }
  .card {
    position: relative;
    width: 525px;
    height: 300px;
    background: var(--paper);
    overflow: hidden;
    box-shadow: 0 12px 30px rgba(0,0,0,.45);
  }

  /* Front */
  .front-photo {
    position: absolute; left: 0; top: 0; width: 100%; height: 172px;
    background: linear-gradient(135deg, #f4f9ee 0%, #dcebc8 45%, #eef5e4 70%, #d3e6bb 100%);
  }
  .front-brand {
    position: absolute; left: 150px; top: 70px;
    display: flex; align-items: center; gap: 10px;
  }
  .brand-square { width: 22px; height: 22px; background: var(--leaf); }
  .brand-name {
    font-weight: 700; font-size: 30px; color: var(--leaf); letter-spacing: -.5px;
  }
  .front-rule {
    position: absolute; left: 0; top: 166px; width: 100%; height: 12px; background: var(--ink);
  }
  .block { position: absolute; display: flex; align-items: center; font-size: 13px; }
  .block b { font-weight: 700; margin-right: 5px; }
  .block-mobile { left: 0; top: 178px; width: 158px; height: 66px; background: var(--leaf); color: var(--paper); padding-left: 12px; }
  .block-office { left: 158px; top: 244px; width: 168px; height: 40px; background: var(--ink); color: var(--paper); padding-left: 16px; }
  .block-fax { left: 326px; top: 250px; width: 199px; height: 50px; background: var(--leaf); color: var(--paper); padding-left: 18px; }
  .holder {
    position: absolute; left: 172px; top: 186px; right: 16px;
    display: flex; justify-content: space-between; align-items: baseline;
  }
  .holder-name { font-weight: 700; font-size: 15px; color: var(--ink); letter-spacing: .5px; text-transform: uppercase; }
  .holder-company { font-size: 13px; color: var(--ink); }
  .holder-email { position: absolute; left: 172px; top: 214px; font-size: 13px; color: var(--ink); }
  .holder-email b { font-weight: 700; }

  /* Back */
  .back-topline { position: absolute; left: 0; top: 0; width: 100%; height: 8px; background: var(--ink); }
  .back-photo {
    position: absolute; left: 0; top: 8px; width: 100%; height: 120px;
    background: linear-gradient(120deg, #9fd84a 0%, #5fa51c 35%, #b6e26d 60%, #3f7f12 100%);
  }
  .back-brand {
    position: absolute; left: 0; right: 0; top: 155px;
    display: flex; justify-content: center; align-items: center; gap: 10px;
  }
  .back-brand .brand-name { font-size: 28px; }
  .website {
    position: absolute; left: 0; right: 0; top: 210px; text-align: center;
    font-size: 16px; font-weight: 700; color: var(--ink);
  }
  .website span { color: var(--leaf); }
  .back-base { position: absolute; left: 0; bottom: 0; width: 100%; height: 14px; }
  .back-base .seg { position: absolute; top: 0; height: 100%; }
  .seg-green-a { left: 0; width: 190px; background: var(--leaf); height: 6px !important; top: 8px !important; }
  .seg-black { left: 190px; width: 120px; background: var(--ink); }
  .seg-green-b { left: 310px; width: 215px; background: var(--leaf); }
</style>
</head>
<body>
  <section class="card card-front">
    <div class="front-photo" role="img" aria-label="Soft faded photo of sunlit green leaves"></div>
    <div class="front-brand">
      <span class="brand-square"></span>
      <span class="brand-name">Bright Parcel Route</span>
    </div>
    <div class="front-rule"></div>
    <div class="block block-mobile"><b>Mobile:</b> 917-555-4862</div>
    <div class="holder">
      <span class="holder-name">Glen Harwick</span>
      <span class="holder-company">Bright Parcel Route</span>
    </div>
    <div class="holder-email"><b>Email:</b> info@brightparcelroute.example</div>
    <div class="block block-office"><b>Office:</b> 516-555-7104</div>
    <div class="block block-fax"><b>Fax:</b> 866-555-3927</div>
  </section>

  <section class="card card-back">
    <div class="back-topline"></div>
    <div class="back-photo" role="img" aria-label="Photo of bright green leaves on a branch in sunlight"></div>
    <div class="back-brand">
      <span class="brand-square"></span>
      <span class="brand-name">Bright Parcel Route</span>
    </div>
    <div class="website">www.<span>brightparcelroute</span>.example</div>
    <div class="back-base">
      <div class="seg seg-green-a"></div>
      <div class="seg seg-black"></div>
      <div class="seg seg-green-b"></div>
    </div>
  </section>
</body>
</html>
```